Web Design Project

My site is already up - www.brightwell-hub.com but is very basic at this stage.
I need a to make the design look better and lift it a bit.
I have my own ideas about what I want.
The target market for the site is women - mainly professional, corporate women around the world aged between 28-40 yrs or thereabouts.
There are 3 main areas the site will focus on:
1: Blog and Inbox magazine with contributing writers on various topics from food, diet, emotional intelligence, intuition, feminine energy sexual and non, money to name a few.
2. There is an Ebook that is being added to the site later this year taking a deeper look at all of these topics. For now those subscribing get a free summary of the book.
Book called "Marigold - Your Gentle Guide to a Calmer Rhythm"
Happy to use the title for the FREE summary for subscribers.
3. Events / retreats. We are kicking off with our first Brightwell-hub retreat in Bali in late Oct 2012. We have amazing shots of the villa we will use and the activities etc that will make up a part of the retreat.
Yoga & meditation
Surfing
Photography
Keen to see what you all come up with.
NOTE: I dont want anything too busy. Keep it fairly clean, simple and in keeping with the general look and feel right now.
Updates
Target Market(s)
Look and feel
Each slider illustrates characteristics of the customer's brand and the style your logo design should communicate.

```html
<!DOCTYPE html>
<html lang="en">
<head>
<meta charset="utf-8">
<title>brightwell-hub.com</title>
<link rel="stylesheet" href="https://fonts.googleapis.com/css2?family=Open+Sans:wght@400;600&family=Tinos:ital@1&display=swap">
<style>
  :root {
    --yellow: #f7d40a;
    --yellow-deep: #e3b904;
    --olive: #6f5f0a;
    --olive-dark: #5b4c05;
    --text: #454545;
    --grey-line: #d6d6d6;
    --white: #ffffff;
    --frame: #e8e2c0;
    --arrow: #c2ad4a;
  }
  html, body { margin: 0; padding: 0; overflow: hidden; background: var(--white); }
  .canvas {
    position: relative; width: 1038px; height: 1200px; overflow: hidden;
    background: var(--white); font-family: "Open Sans", Verdana, sans-serif; color: var(--text);
  }
  .abs { position: absolute; }
  .header-wave, .hero-wave, .footer-wave { position: absolute; left: 0; width: 1038px; }
  .header-wave { top: 0; height: 200px; }
  .brand { top: 78px; left: 133px; display: flex; align-items: center; gap: 10px;
    color: var(--white); font-size: 31px; font-weight: 400; letter-spacing: 0.3px; }
  .brand-dot { width: 40px; height: 40px; border-radius: 50%; background: var(--white); opacity: .9; }
  .login { top: 90px; left: 597px; font-size: 16px; color: var(--olive); text-decoration: underline; }
  .hero-photo-main { top: 160px; left: 620px; width: 262px; height: 390px;
    border-radius: 130px 130px 0 0;
    background: linear-gradient(170deg, #6b4a30 0%, #c99a7c 35%, #e7c3a8 55%, #8fa3b0 80%, #6f8796 100%); }
  .hero-photo-group { top: 345px; left: 450px; width: 170px; height: 195px;
    border-radius: 60px 60px 0 0;
    background: linear-gradient(180deg, #6a5a52 0%, #3c3c44 40%, #2c2c32 100%); }
  .quote { top: 264px; left: 107px; font-family: "Tinos", "Times New Roman", serif; font-style: italic;
    font-size: 25px; color: #3a3a3a; }
  .quote-by { top: 299px; left: 105px; font-family: "Tinos", "Times New Roman", serif; font-style: italic;
    font-size: 14px; color: #3a3a3a; }
  .btn-learn { top: 372px; left: 106px; width: 159px; height: 38px; border-radius: 3px;
    background: linear-gradient(90deg, var(--olive-dark), #9c8a1d 55%, #d1bd4a);
    color: var(--white); font-size: 15px; line-height: 38px; text-align: center; }
  .dots { top: 473px; left: 195px; display: flex; gap: 10px; }
  .dot { width: 16px; height: 16px; border-radius: 50%; background: #9a9a9a; }
  .dot.active { background: var(--yellow); }
  .hero-wave { top: 480px; height: 110px; }
  .nav { top: 525px; left: 84px; width: 643px; height: 92px; display: flex;
    background: linear-gradient(180deg, #f1cf18 0%, var(--yellow) 45%, var(--yellow-deep) 100%);
    border-radius: 0 0 8px 8px; padding-top: 24px; box-sizing: border-box; }
  .nav a { color: var(--white); font-size: 19px; text-decoration: none; padding: 26px 0 0 0;
    border-right: 1px solid rgba(255,255,255,.45); box-sizing: border-box; text-align: center; }
  .nav a:last-child { border-right: none; }
  .section-title { font-size: 23px; font-weight: 400; color: #555; margin: 0; }
  .section-title .accent { color: var(--olive); }
  .rule { height: 4px; background: var(--grey-line); }
  .welcome-title { top: 652px; left: 88px; }
  .welcome-rule { top: 690px; left: 84px; width: 643px; }
  .welcome-icon { top: 721px; left: 85px; width: 88px; height: 75px; border-radius: 6px;
    background: linear-gradient(135deg, #4a4a3a, #8c8a6a 50%, #2e2e24); }
  .welcome-text { top: 706px; left: 180px; width: 542px; font-size: 12.5px; line-height: 20px;
    letter-spacing: 1.1px; text-align: justify; margin: 0; }
  .btn-more { top: 860px; left: 652px; width: 70px; height: 25px; border-radius: 3px;
    background: linear-gradient(180deg, #a48d17, var(--olive)); color: #f4e7a8; font-size: 11px;
    line-height: 25px; text-align: center; }
  .activities-title { top: 880px; left: 88px; }
  .activities-rule { top: 917px; left: 84px; width: 643px; }
  .carousel { top: 932px; left: 83px; width: 645px; height: 145px; box-sizing: border-box;
    border: 5px solid var(--frame); border-radius: 6px; background: var(--white); }
  .carousel-arrow { position: absolute; top: 0; bottom: 0; width: 29px; background: var(--arrow); }
  .carousel-arrow.prev { left: 0; } .carousel-arrow.next { right: 0; }
  .carousel-arrow svg { position: absolute; top: 56px; left: 8px; }
  .thumb { position: absolute; top: 14px; height: 102px; border: 3px solid #d9cf9c; box-sizing: border-box; }
  .thumb-yoga { left: 41px; width: 147px; background: linear-gradient(135deg, #3a2e20, #7a5e40 50%, #2a2218); }
  .thumb-camera { background: linear-gradient(180deg, #d6d6d6, #8a8a8a 55%, #bdbdbd); }
  .thumb-camera.one { left: 196px; width: 136px; }
  .thumb-camera.two { left: 460px; width: 137px; }
  .thumb-surf { left: 344px; width: 103px; background: linear-gradient(180deg, #c9d4da, #d9d1c0 55%, #b9a98a); }
  .blogs-title { top: 655px; left: 752px; color: var(--olive); }
  .blogs-rule { top: 690px; left: 752px; width: 251px; }
  .blog-post { left: 754px; width: 252px; font-size: 12.5px; line-height: 20px; letter-spacing: 1.1px;
    text-align: justify; margin: 0; }
  .read-more { display: block; text-align: right; font-weight: 600; color: #888; }
  .read-more u { letter-spacing: 1px; }
  .footer-wave { top: 1095px; height: 105px; }
  .copyright { top: 1165px; left: 90px; font-size: 10px; color: #5a5a5a; }
  .copyright a { color: var(--white); font-weight: 600; }
  .footer-nav { top: 1161px; right: 40px; font-size: 16px; color: #6a5a0a; }
</style>
</head>
<body>
<div class="canvas">

  <svg class="header-wave" viewBox="0 0 1038 200" aria-hidden="true">
    <defs>
      <linearGradient id="headerFill" x1="0" y1="0" x2="0" y2="1">
        <stop offset="0" stop-color="#f8d508"/>
        <stop offset="1" stop-color="#f3cc06"/>
      </linearGradient>
    </defs>
    <path d="M0 0 H1038 V46 C820 46 640 196 380 188 C220 184 100 150 0 138 Z" fill="#fbe98a"/>
    <path d="M0 0 H1038 V38 C820 40 640 186 380 178 C220 174 100 140 0 128 Z" fill="url(#headerFill)"/>
  </svg>

  <div class="abs brand"><span class="brand-dot"></span>brightwell-hub.com</div>
  <div class="abs login">Login/ Register</div>

  <div class="abs hero-photo-group" role="img" aria-label="Photo of a small group of business people in suits"></div>
  <div class="abs hero-photo-main" role="img" aria-label="Photo of a smiling professional woman"></div>

  <div class="abs quote">‘The Western Women will change the World”</div>
  <div class="abs quote-by">- Anna Whitfield</div>
  <div class="abs btn-learn">&gt;&gt; Learn More</div>
  <div class="abs dots"><span class="dot"></span><span class="dot active"></span><span class="dot"></span></div>

  <svg class="hero-wave" viewBox="0 0 1038 110" aria-hidden="true">
    <defs>
      <linearGradient id="shade" x1="0" y1="0" x2="0" y2="1">
        <stop offset="0" stop-color="#e6e6e6"/>
        <stop offset="1" stop-color="#ffffff"/>
      </linearGradient>
    </defs>
    <path d="M0 56 C120 30 250 22 420 42 S800 74 1038 70 V110 H0 Z" fill="url(#shade)"/>
    <path d="M0 56 C120 30 250 22 420 42 S800 74 1038 70" fill="none" stroke="#f3dc6a" stroke-width="6"/>
  </svg>

  <nav class="abs nav">
    <a style="width:104px">Home</a>
    <a style="width:90px">About</a>
    <a style="width:78px">Blog</a>
    <a style="width:140px">Community</a>
    <a style="width:112px">Retreats</a>
    <a style="width:119px">Contact</a>
  </nav>

  <h2 class="abs section-title welcome-title"><span class="accent">Welcome</span> to our site</h2>
  <div class="abs rule welcome-rule"></div>
  <div class="abs welcome-icon" role="img" aria-label="Small image of a dark metallic tablet device"></div>
  <p class="abs welcome-text">The Willow Lane Event Center is looking for a website design. We specialize in all types of events from weddings to company outings. We have an amazing rustic barn to fit any service and can also provide a complete multi-unit home that includes.<br>10 bedrooms (sleeps 20 comfortably), 5 full bathis a professional chef style and 1 full professional outdoor kitchen. The Willow Lane Event Center is looking for a website design. We specialize in all types of events from weddings to company outings.</p>
  <div class="abs btn-more">&#9654; More</div>

  <h2 class="abs section-title activities-title"><span class="accent">Our</span> activities</h2>
  <div class="abs rule activities-rule"></div>
  <div class="abs carousel">
    <div class="carousel-arrow prev"><svg width="12" height="24" viewBox="0 0 12 24"><path d="M10 2 L3 12 L10 22" fill="none" stroke="#fff" stroke-width="2"/></svg></div>
    <div class="thumb thumb-yoga" role="img" aria-label="Yoga pose on a stage under warm lights"></div>
    <div class="thumb thumb-camera one" role="img" aria-label="Photographer holding a camera"></div>
    <div class="thumb thumb-surf" role="img" aria-label="Two surfers walking on the beach"></div>
    <div class="thumb thumb-camera two" role="img" aria-label="Photographer holding a camera"></div>
    <div class="carousel-arrow next"><svg width="12" height="24" viewBox="0 0 12 24"><path d="M2 2 L9 12 L2 22" fill="none" stroke="#fff" stroke-width="2"/></svg></div>
  </div>

  <h2 class="abs section-title blogs-title">Blogs</h2>
  <div class="abs rule blogs-rule"></div>
  <p class="abs blog-post" style="top:702px">Our blog is proud to announce that it is the Gold Sponsor of the NWL Leaders Summit 2010<br>Wednesday, April 7, 2010<span class="read-more"><u>Read More</u> &gt;&gt;</span></p>
  <p class="abs blog-post" style="top:837px">Our blog is proud to announce that it is the Gold Sponsor of the NWL Leaders Summit 2010<br>Wednesday, April 7, 2010<span class="read-more"><u>Read More</u> &gt;&gt;</span></p>
  <p class="abs blog-post" style="top:972px">Our blog is proud to announce that it is the Gold Sponsor of the NWL Leaders Summit 2010<br>Wednesday, April 7, 2010<span class="read-more"><u>Read More</u> &gt;&gt;</span></p>

  <svg class="footer-wave" viewBox="0 0 1038 105" aria-hidden="true">
    <defs>
      <linearGradient id="footerFill" x1="0" y1="0" x2="0" y2="1">
        <stop offset="0" stop-color="#fbf1b8"/>
        <stop offset=".35" stop-color="#f6d84a"/>
        <stop offset="1" stop-color="#e4b806"/>
      </linearGradient>
    </defs>
    <path d="M0 28 C300 6 700 2 1038 40 V105 H0 Z" fill="url(#footerFill)"/>
  </svg>
  <div class="abs copyright">Copyright @ 2012, <a>brightwell-hub.com</a></div>
  <div class="abs footer-nav">Home &nbsp;|&nbsp; About &nbsp;|&nbsp; Blog &nbsp;|&nbsp; Community &nbsp;|&nbsp; Retreats &nbsp;|&nbsp; Contact</div>

</div>
</body>
</html>
```